Corporate Trainning business needs PPT template for sales, reports and projects

Create a power point template with own design and rich in distinctness of our brand, logo and industry (corporate training). Enough slides templates to use for sales, reports and projects development: flowcharts, roadmaps, bullets, service categories, description box, title & subtitle slides, bar & pie charts, calendars, gantt, some basic shapes and icons (training, education, elearning, etc related).
Enclose: color palette, set of logo for different uses and ppt presentation with some ideas and slide templates. The ppt hope could help, but I trust in your experience and creativity.

Target Market(s)

Company training

Industry/Entity Type

Training - Education

Font styles to use
Sans Serif

Requirements
Nice to have
• Relative to training icons

```html
<!DOCTYPE html>
<html lang="en">
<head>
<meta charset="utf-8">
<title>Veranta – Corporate Training Presentation Template</title>
<link href="https://fonts.googleapis.com/css2?family=Roboto:wght@400;500;700;900&display=swap" rel="stylesheet">
<style>
:root{
  --canvas:#9a9d9f;
  --paper:#f3f3f6;
  --navy:#13223f;
  --yellow:#e6be1f;
  --ink:#1c2740;
  --muted:#3a4258;
  --white:#ffffff;
}
*{box-sizing:border-box;margin:0;padding:0}
html,body{width:1200px;height:3713px;overflow:hidden}
body{background:var(--canvas);font-family:'Roboto',Arial,sans-serif;color:var(--ink);position:relative}
.slide{position:absolute;left:101px;width:1002px;height:562px;background:var(--paper);overflow:hidden}
.abs{position:absolute}

/* brand wordmark */
.brand{position:absolute;display:flex;align-items:center;gap:10px;height:42px}
.brand__dot{width:30px;height:30px;border-radius:50%;background:var(--yellow)}
.brand__name{font-family:'Roboto',Arial,sans-serif;font-weight:400;font-size:40px;color:var(--navy);letter-spacing:.5px;line-height:1}

.divider{position:absolute;width:2px;height:50px;background:var(--yellow)}
.heading{position:absolute;font-weight:700;font-size:26px;line-height:31px;letter-spacing:.5px;color:var(--navy)}
.heading span{display:block;color:var(--yellow)}

/* cover */
.cover{top:52px;height:563px}
.cover__photo{position:absolute;inset:0;background:linear-gradient(180deg,#6d9fd3 0%,#a9c3d8 22%,#8a8f92 45%,#6f8a55 70%,#4f7a3c 88%,#2f6d68 100%)}
.cover__brand{left:713px;top:42px}
.cover__title{position:absolute;left:0;right:0;text-align:center;color:var(--white);font-weight:900;text-shadow:0 2px 6px rgba(0,0,0,.45)}
.cover__kicker{top:226px;font-size:36px;font-weight:700;letter-spacing:1px}
.cover__main{top:268px;font-size:84px;letter-spacing:2px}

/* solutions */
.solutions{top:651px}
.solutions__title{position:absolute;left:0;right:0;top:78px;text-align:center;font-weight:700;font-size:24px;letter-spacing:.5px;color:var(--navy)}
.solutions__title span{color:var(--yellow)}
.service{position:absolute;width:301px;height:163px;color:var(--white);text-align:center}
.service__shape{position:absolute;inset:0}
.service__icon{position:absolute;left:132px;top:20px;width:38px;height:38px}
.service__name{position:absolute;left:0;right:0;top:75px;font-weight:700;font-size:16px;letter-spacing:.3px}
.service__text{position:absolute;left:0;right:0;top:101px;font-size:13.5px;line-height:19px}

/* chart */
.report{top:1246px}
.report__chart{position:absolute;left:0;top:0;width:1002px;height:562px}
.report__text{position:absolute;left:696px;top:263px;width:265px;font-size:14px;line-height:21px;color:var(--ink)}

/* flow */
.flow{top:1848px}
.flow__lines{position:absolute;left:0;top:0;width:1002px;height:562px}
.step{position:absolute;width:210px;text-align:center;top:188px}
.step__icon{display:block;margin:0 auto;width:50px;height:50px}
.step__name{margin-top:16px;font-weight:700;font-size:16px;color:var(--navy);letter-spacing:.3px}
.step__text{margin-top:10px;font-size:11.6px;line-height:15.8px;color:var(--ink)}

/* programmes */
.programmes{top:2450px}
.programme{position:absolute;width:300px;text-align:center;top:140px}
.programme__visual{position:relative;width:266px;height:266px;margin:0 auto;border-radius:50%;background:radial-gradient(circle at 45% 40%,#2a3d63 0%,#172a4c 55%,#10203c 100%);overflow:hidden}
.programme__icon{position:absolute;left:83px;top:83px;width:100px;height:100px}
.programme__name{margin-top:26px;font-weight:700;font-size:16px;color:var(--navy);letter-spacing:.3px}
.programme__text{margin-top:8px;font-size:11.8px;line-height:15.5px;color:var(--ink)}

/* feature */
.feature{top:3048px;height:564px}
.feature__band{position:absolute;left:0;right:0;top:122px;height:21px;background:var(--yellow)}
.feature__panel{position:absolute;left:0;right:0;top:143px;bottom:0;background:var(--navy)}
.feature__photo{position:absolute;left:23px;top:169px;width:519px;height:370px;background:radial-gradient(ellipse at 50% 40%,#8d8d86 0%,#4c5152 45%,#2a2f31 100%)}
.feature__title{position:absolute;left:598px;top:232px;font-weight:700;font-size:25px;line-height:31px;color:var(--white);letter-spacing:.5px}
.feature__text{position:absolute;left:598px;top:315px;width:340px;font-size:17px;line-height:22px;color:#dfe3ec}
</style>
</head>
<body>

<!-- Cover -->
<section class="slide cover">
  <div class="cover__photo" role="img" aria-label="Aerial photo of a modern city skyline with high-rise towers, a green park and a lake"></div>
  <div class="brand cover__brand"><span class="brand__dot"></span><span class="brand__name">Veranta</span></div>
  <div class="cover__title cover__kicker">WELCOME TO</div>
  <div class="cover__title cover__main">VERANTA</div>
</section>

<!-- Solutions -->
<section class="slide solutions">
  <div class="brand" style="left:35px;top:34px"><span class="brand__dot"></span><span class="brand__name">Veranta</span></div>
  <h2 class="solutions__title">VERANTA <span>SOLUTIONS</span></h2>

  <div class="service" style="left:35px;top:156px">
    <svg class="service__shape" viewBox="0 0 301 163" preserveAspectRatio="none"><path d="M0 22 Q150.5 -22 301 22 V163 H0Z" fill="var(--navy)"/></svg>
    <svg class="service__icon" viewBox="0 0 38 38" fill="none" stroke="var(--yellow)" stroke-width="2.4" stroke-linejoin="round"><path d="M20 4 H33 V17 L17 33 L4 20Z"/><circle cx="27" cy="10" r="2.3"/><path d="M15 19 L21 13 M17 23 L23 17"/></svg>
    <div class="service__name">BRAND ID</div>
    <div class="service__text">lorem ipsum dolor sit amet,<br>conse ctetuer adipiscing elit.</div>
  </div>
  <div class="service" style="left:347px;top:156px">
    <svg class="service__shape" viewBox="0 0 301 163" preserveAspectRatio="none"><path d="M0 22 Q150.5 -22 301 22 V163 H0Z" fill="var(--navy)"/></svg>
    <svg class="service__icon" viewBox="0 0 38 38" fill="var(--yellow)"><path d="M33 5 C24 5 17 10 13 18 L20 25 C28 21 33 14 33 5Z"/><path d="M12 19 L6 19 L11 13 L17 13Z M19 26 L19 32 L25 27 L25 21Z"/><path d="M10 24 L5 33 L14 28Z"/></svg>
    <div class="service__name">STARTUP SUPPORT</div>
    <div class="service__text">lorem ipsum dolor sit amet,<br>conse ctetuer adipiscing elit.</div>
  </div>
  <div class="service" style="left:664px;top:156px">
    <svg class="service__shape" viewBox="0 0 301 163" preserveAspectRatio="none"><path d="M0 22 Q150.5 -22 301 22 V163 H0Z" fill="var(--navy)"/></svg>
    <svg class="service__icon" viewBox="0 0 38 38" fill="none" stroke="var(--yellow)" stroke-width="2.4" stroke-linecap="round"><path d="M8 6 L14 6 L16 13 L12 16 C14 21 17 24 22 26 L25 22 L32 24 L32 30 C32 32 30 33 28 33 C16 32 6 22 5 10 C5 8 6 6 8 6Z" fill="var(--yellow)" stroke="none"/><path d="M22 9 A7 7 0 0 1 29 16 M22 4 A12 12 0 0 1 34 16"/></svg>
    <div class="service__name">CALL CENTER</div>
    <div class="service__text">lorem ipsum dolor sit amet,<br>conse ctetuer adipiscing elit.</div>
  </div>

  <div class="service" style="left:35px;top:341px">
    <svg class="service__shape" viewBox="0 0 301 163" preserveAspectRatio="none"><path d="M0 22 Q150.5 -22 301 22 V163 H0Z" fill="var(--navy)"/></svg>
    <svg class="service__icon" viewBox="0 0 38 38" fill="none" stroke="var(--yellow)" stroke-width="2.4" stroke-linecap="round"><circle cx="16" cy="16" r="11"/><path d="M24 24 L34 34"/><circle cx="11" cy="19" r="1.8" fill="var(--yellow)"/><circle cx="16" cy="12" r="1.8" fill="var(--yellow)"/><circle cx="21" cy="18" r="1.8" fill="var(--yellow)"/><path d="M11 19 L16 12 L21 18" stroke-width="1.5"/></svg>
    <div class="service__name">MARKET RESEARCH</div>
    <div class="service__text">lorem ipsum dolor sit amet,<br>conse ctetuer adipiscing elit.</div>
  </div>
  <div class="service" style="left:347px;top:341px">
    <svg class="service__shape" viewBox="0 0 301 163" preserveAspectRatio="none"><path d="M0 22 Q150.5 -22 301 22 V163 H0Z" fill="var(--navy)"/></svg>
    <svg class="service__icon" viewBox="0 0 38 38" fill="none" stroke="var(--yellow)" stroke-width="2.2"><circle cx="19" cy="19" r="13"/><ellipse cx="19" cy="19" rx="6" ry="13"/><path d="M6 19 H32 M9 12 H29 M9 26 H29"/></svg>
    <div class="service__name">SECURITY CONTROL</div>
    <div class="service__text">lorem ipsum dolor sit amet,<br>conse ctetuer adipiscing elit.</div>
  </div>
  <div class="service" style="left:664px;top:341px">
    <svg class="service__shape" viewBox="0 0 301 163" preserveAspectRatio="none"><path d="M0 22 Q150.5 -22 301 22 V163 H0Z" fill="var(--navy)"/></svg>
    <svg class="service__icon" viewBox="0 0 38 38" fill="none" stroke="var(--yellow)" stroke-width="2.4"><circle cx="28" cy="8" r="4.5"/><circle cx="9" cy="19" r="4.5"/><circle cx="28" cy="30" r="4.5"/><path d="M13 17 L24 10 M13 21 L24 28"/></svg>
    <div class="service__name">SOCIAL MEDIA</div>
    <div class="service__text">lorem ipsum dolor sit amet,<br>conse ctetuer adipiscing elit.</div>
  </div>
</section>

<!-- Bar chart report -->
<section class="slide report">
  <div class="brand" style="left:52px;top:32px"><span class="brand__dot"></span><span class="brand__name">Veranta</span></div>
  <div class="divider" style="left:269px;top:30px"></div>
  <h2 class="heading" style="left:302px;top:26px">LOREM IPSUM IS<span>SIMPLY DUMMY</span></h2>

  <svg class="report__chart" viewBox="0 0 696 390" role="img" aria-label="Bar chart comparing two series across four categories">
    <g font-family="Roboto, Arial, sans-serif" font-size="7" fill="var(--ink)" text-anchor="middle">
      <text x="37" y="84">6</text><text x="37" y="125">5</text><text x="37" y="167">4</text>
      <text x="37" y="208">3</text><text x="37" y="250">2</text><text x="37" y="291">1</text><text x="37" y="333">0</text>
    </g>
    <g fill="var(--navy)">
      <rect x="85" y="273" width="23" height="64"/><rect x="184" y="196" width="23" height="141"/>
      <rect x="274" y="303" width="23" height="34"/><rect x="379" y="238" width="23" height="99"/>
    </g>
    <g fill="var(--yellow)">
      <rect x="112" y="239" width="23" height="98"/><rect x="211" y="122" width="23" height="215"/>
      <rect x="301" y="285" width="23" height="52"/><rect x="406" y="185" width="23" height="152"/>
    </g>
    <path d="M52 75 V337 H468" fill="none" stroke="var(--navy)" stroke-width="2"/>
    <g font-family="Roboto, Arial, sans-serif" font-size="7.5" font-weight="700" fill="var(--navy)" text-anchor="middle">
      <text x="106" y="358">LOREM</text><text x="205" y="358">LOREM</text><text x="298" y="358">LOREM</text><text x="398" y="358">LOREM</text>
    </g>
  </svg>

  <p class="report__text">There are many variations of passages of Lorem Ipsum available, but the majority have suffered alteration in some form, by injected humour, or randomised words which don't look even slightly believable. If you are going to use a passage of Lorem Ipsum, you need to be sure there isn't anything embarrassing hidden in the middle of text.</p>
</section>

<!-- Process flow -->
<section class="slide flow">
  <div class="brand" style="left:49px;top:39px"><span class="brand__dot"></span><span class="brand__name">Veranta</span></div>
  <div class="divider" style="left:272px;top:37px"></div>
  <h2 class="heading" style="left:317px;top:33px">LOREM IPSUM IS<span>SIMPLY DUMMY</span></h2>

  <svg class="flow__lines" viewBox="0 0 696 390" aria-hidden="true">
    <defs>
      <linearGradient id="g1" gradientUnits="userSpaceOnUse" x1="34" y1="105" x2="230" y2="353"><stop offset="0" stop-color="#f0441c"/><stop offset=".35" stop-color="#f5a51c"/><stop offset=".7" stop-color="#3faa6a"/><stop offset="1" stop-color="#1b8fd8"/></linearGradient>
      <linearGradient id="g2" gradientUnits="userSpaceOnUse" x1="229" y1="105" x2="454" y2="353"><stop offset="0" stop-color="#1b6ee0"/><stop offset=".55" stop-color="#9b2fa8"/><stop offset="1" stop-color="#e5246b"/></linearGradient>
      <linearGradient id="g2b" gradientUnits="userSpaceOnUse" x1="259" y1="287" x2="454" y2="222"><stop offset="0" stop-color="#e5246b"/><stop offset=".5" stop-color="#8a35b5"/><stop offset="1" stop-color="#1b6ee0"/></linearGradient>
      <linearGradient id="g3" gradientUnits="userSpaceOnUse" x1="483" y1="105" x2="649" y2="353"><stop offset="0" stop-color="#17a89a"/><stop offset=".45" stop-color="#8fb23a"/><stop offset=".75" stop-color="#f3b41a"/><stop offset="1" stop-color="#f0441c"/></linearGradient>
    </defs>
    <g fill="none" stroke-width="3" stroke-linejoin="round">
      <path d="M200 169 V121 Q200 105 184 105 H50 Q34 105 34 121 V337 Q34 353 50 353 H184 Q200 353 200 337 V262 L229 222" stroke="url(#g1)"/>
      <path d="M229 222 L259 182 V121 Q259 105 275 105 H408 Q424 105 424 121 V169" stroke="url(#g2)"/>
      <path d="M259 287 V337 Q259 353 275 353 H408 Q424 353 424 337 V262 L454 222" stroke="url(#g2b)"/>
      <path d="M454 222 L483 182 V121 Q483 105 499 105 H633 Q649 105 649 121 V337 Q649 353 633 353 H499 Q483 353 483 337 V287" stroke="url(#g3)"/>
    </g>
    <circle cx="200" cy="169" r="6.5" fill="#f2c21b"/>
    <circle cx="424" cy="169" r="6.5" fill="#e5246b"/>
    <circle cx="259" cy="287" r="6.5" fill="#e5246b"/>
    <circle cx="483" cy="287" r="6.5" fill="#f2c21b"/>
  </svg>

  <div class="step" style="left:64px">
    <svg class="step__icon" viewBox="0 0 50 50" fill="none" stroke="var(--yellow)" stroke-width="3"><circle cx="25" cy="11" r="5"/><circle cx="11" cy="36" r="5"/><circle cx="39" cy="36" r="5"/><path d="M17 12 A16 16 0 0 0 9 27 M33 12 A16 16 0 0 1 41 27 M17 43 A16 16 0 0 0 33 43"/></svg>
    <div class="step__name">LOREM IPSUM</div>
    <p class="step__text">There are many variations of passages of Lorem Ipsum availa ble, but the majority have suffered alteration in some form, by injec ted humour, or randomised words which don't look even slightly believable. If you are going to use a passage of Lorem Ipsum, you need to be sure there isn't anything embarrassing hidden in the middle of text. All the Lorem</p>
  </div>
  <div class="step" style="left:387px">
    <svg class="step__icon" viewBox="0 0 50 50" fill="var(--yellow)"><path d="M21 3 H29 L30 10 L35 12 L41 8 L46 14 L41 19 L43 24 L50 25 V29 L43 31 L41 36 L46 41 L40 47 L35 42 L30 44 L29 50 H21 L20 44 L15 42 L10 47 L4 41 L9 36 L7 31 L0 29 V25 L7 24 L9 19 L4 14 L10 8 L15 12 L20 10Z M25 18 A9 9 0 1 0 25.01 18Z" transform="scale(.92) translate(2 0)" fill-rule="evenodd"/></svg>
    <div class="step__name">LOREM IPSUM</div>
    <p class="step__text">There are many variations of passages of Lorem Ipsum availa ble, but the majority have suffered alteration in some form, by injec ted humour, or randomised words which don't look even slightly believable. If you are going to use a passage of Lorem Ipsum, you need to be sure there isn't anything embarrassing hidden in the middle of text. All the Lorem</p>
  </div>
  <div class="step" style="left:710px">
    <svg class="step__icon" viewBox="0 0 50 50" fill="var(--yellow)"><path d="M25 3 A15 15 0 0 0 16 30 V36 H34 V30 A15 15 0 0 0 25 3Z"/><rect x="17" y="39" width="16" height="3.5" rx="1.5"/><rect x="19" y="45" width="12" height="3.5" rx="1.5"/><path d="M21 18 L25 23 L29 18 M25 23 V34" fill="none" stroke="var(--paper)" stroke-width="2.4"/></svg>
    <div class="step__name">LOREM IPSUM</div>
    <p class="step__text">There are many variations of passages of Lorem Ipsum availa ble, but the majority have suffered alteration in some form, by injec ted humour, or randomised words which don't look even slightly believable. If you are going to use a passage of Lorem Ipsum, you need to be sure there isn't anything embarrassing hidden in the middle of text. All the Lorem</p>
  </div>
</section>

<!-- Programmes -->
<section class="slide programmes">
  <div class="brand" style="left:49px;top:39px"><span class="brand__dot"></span><span class="brand__name">Veranta</span></div>
  <div class="divider" style="left:272px;top:37px"></div>
  <h2 class="heading" style="left:317px;top:33px">LOREM IPSUM IS<span>SIMPLY DUMMY</span></h2>

  <div class="programme" style="left:33px">
    <div class="programme__visual" role="img" aria-label="Dark blue tinted photo of a classroom training session">
      <svg class="programme__icon" viewBox="0 0 100 100" fill="none" stroke="var(--yellow)" stroke-width="5" stroke-linecap="round"><rect x="18" y="18" width="66" height="44"/><path d="M30 50 L44 38 L54 46 L72 30"/><path d="M51 62 V74 M51 66 L34 92 M51 66 L68 92 M51 8 V18"/></svg>
    </div>
    <div class="programme__name">TRAINING</div>
    <p class="programme__text">There are many variations of passages of Lorem Ipsum availa ble, but the majority have suffered alteration in some form, by injec ted humour, or randomised words which don't.</p>
  </div>
  <div class="programme" style="left:351px">
    <div class="programme__visual" role="img" aria-label="Dark blue tinted photo of students in a lecture hall">
      <svg class="programme__icon" viewBox="0 0 100 100" fill="var(--yellow)"><path d="M8 20 H14 V78 H44 C47 78 49 80 50 82 C51 80 53 78 56 78 H86 V20 H92 V86 H56 L50 90 L44 86 H8Z"/><path d="M20 14 H40 C45 14 47 17 47 21 V78 C45 74 42 72 38 72 H20Z M80 14 H60 C55 14 53 17 53 21 V78 C55 74 58 72 62 72 H80Z"/></svg>
    </div>
    <div class="programme__name">EDUCATION</div>
    <p class="programme__text">There are many variations of passages of Lorem Ipsum availa ble, but the majority have suffered alteration in some form, by injec ted humour, or randomised words which don't.</p>
  </div>
  <div class="programme" style="left:664px">
    <div class="programme__visual" role="img" aria-label="Dark blue tinted photo of an open notebook on a desk">
      <svg class="programme__icon" viewBox="0 0 100 100" fill="none" stroke="var(--yellow)" stroke-width="4.5" stroke-linejoin="round" stroke-linecap="round"><path d="M88 10 L14 44 L38 52 Z M88 10 L38 52 L46 76 Z M38 52 L32 66 L46 60"/><path d="M30 72 C18 76 16 84 26 86 C34 88 44 84 52 90" stroke-dasharray="6 6"/></svg>
    </div>
    <div class="programme__name">LEARNING</div>
    <p class="programme__text">There are many variations of passages of Lorem Ipsum availa ble, but the majority have suffered alteration in some form, by injec ted humour, or randomised words which don't.</p>
  </div>
</section>

<!-- Feature -->
<section class="slide feature">
  <div class="brand" style="left:32px;top:38px"><span class="brand__dot"></span><span class="brand__name">Veranta</span></div>
  <div class="divider" style="left:256px;top:34px"></div>
  <h2 class="heading" style="left:301px;top:30px">LOREM IPSUM IS<span>SIMPLY DUMMY</span></h2>
  <div class="feature__band"></div>
  <div class="feature__panel"></div>
  <div class="feature__photo" role="img" aria-label="Photo of a glowing light bulb rising from an open cardboard box on a book, with chalkboard sketches behind"></div>
  <h3 class="feature__title">THERE ARE MANY<br>VARIATIONS OF</h3>
  <p class="feature__text">At vero eos et accusamus et iusto odio dignissimos ducimus qui blanditiis praesentium voluptatum deleniti atque corrupti quos dolores et quas molestias excepturi sint occaecati cupiditate non provident, similique sunt in culpa qui officia deserunt mollitia animi, id est laborum et dolorum fuga.</p>
</section>

</body>
</html>
```